Business Card Design for a Marketing Agency

I will need a business card design for a new marketing agency based in Singapore. We provide marketing and sales solutions to our startup companies. We would like to see the designs to be creative and client friendly. It should display contrast, creative and simple. see: kelvarimedia.com

For the back part please list out all the work done by the company listed in the website

```html
<!DOCTYPE html>
<html lang="en">
<head>
<meta charset="utf-8">
<title>Kelvari Media – Business Card</title>
<link rel="stylesheet" href="https://fonts.googleapis.com/css2?family=Exo+2:wght@400;600;700&display=swap">
<style>
  :root{
    --bg:#2c2c2c;
    --divider:#111111;
    --navy-top:#2b4556;
    --navy-bottom:#1c2b38;
    --teal-top:#1f5f63;
    --teal-bottom:#2a857c;
    --yellow:#d4ab1e;
    --charcoal:#2e2f31;
    --text-light:#e4e4de;
    --text-soft:#c9cbc6;
    --illustration-a:#e0b824;
    --illustration-b:#2aa7a0;
  }
  *{box-sizing:border-box;margin:0;padding:0}
  html,body{width:889px;height:1200px;overflow:hidden}
  body{background:var(--bg);font-family:"Exo 2",sans-serif;position:relative}
  .half{position:absolute;left:0;width:889px;height:598px;display:flex;align-items:center;justify-content:center}
  .half--front{top:0}
  .half--back{top:602px}
  .divider{position:absolute;left:0;top:598px;width:889px;height:4px;background:var(--divider)}

  .card{position:relative;width:560px;height:320px;overflow:hidden;box-shadow:0 10px 24px rgba(0,0,0,.45)}

  /* Front: services */
  .card--front{background:linear-gradient(160deg,var(--navy-top),var(--navy-bottom))}
  .services{list-style:none;position:absolute;left:0;top:22px}
  .service{
    height:32px;margin-bottom:6px;background:var(--yellow);
    display:flex;align-items:center;justify-content:flex-end;padding-right:22px;
    clip-path:polygon(0 0,100% 0,calc(100% - 10px) 100%,0 100%);
    color:var(--text-light);font-weight:700;font-size:20px;letter-spacing:.3px;
    text-shadow:0 1px 1px rgba(0,0,0,.15)
  }
  .service:nth-child(1){width:230px}
  .service:nth-child(2){width:245px}
  .service:nth-child(3){width:262px}
  .service:nth-child(4){width:278px}
  .service:nth-child(5){width:292px}
  .service:nth-child(6){width:306px}
  .service:nth-child(7){width:322px}
  .growth-illustration{
    position:absolute;left:370px;top:70px;width:160px;height:130px;border-radius:10px;
    background:linear-gradient(135deg,var(--illustration-a) 0%,var(--illustration-a) 55%,var(--illustration-b) 100%);
    opacity:.9
  }

  /* Back: contact */
  .card--back{background:linear-gradient(200deg,var(--teal-top),var(--teal-bottom))}
  .brand{position:absolute;right:62px;top:38px;text-align:right}
  .brand__name{font-weight:700;font-size:46px;color:var(--text-soft);letter-spacing:1px;line-height:1}
  .brand__tagline{font-size:13px;color:var(--text-soft);letter-spacing:3px;margin-top:4px}

  .row{position:absolute;display:flex;align-items:center;gap:14px;color:var(--text-light);font-size:15px;font-weight:600}
  .row svg{width:20px;height:20px;flex:none}
  .row--yellow{background:var(--yellow)}
  .row--dark{background:var(--charcoal)}

  .row--mobile{left:308px;top:150px;width:252px;height:40px;justify-content:flex-end;padding-right:16px;
    clip-path:polygon(10px 0,100% 0,100% 100%,0 100%)}
  .row--phone{left:298px;top:190px;width:262px;height:40px;justify-content:flex-end;padding-right:16px;
    clip-path:polygon(10px 0,100% 0,100% 100%,0 100%)}
  .row--address{left:288px;top:230px;width:272px;height:50px;justify-content:flex-end;padding-right:16px;
    clip-path:polygon(10px 0,100% 0,100% 100%,0 100%)}

  .row--name{left:0;top:190px;width:308px;height:40px;padding-left:22px;
    clip-path:polygon(0 0,100% 0,calc(100% - 10px) 100%,0 100%)}
  .row--email{left:0;top:230px;width:298px;height:45px;padding-left:22px;
    clip-path:polygon(0 0,100% 0,calc(100% - 10px) 100%,0 100%)}
  .row--web{left:0;top:275px;width:560px;height:45px;padding-left:22px}
</style>
</head>
<body>

<section class="half half--front">
  <div class="card card--front">
    <ul class="services">
      <li class="service">Telemarketing</li>
      <li class="service">Web Design</li>
      <li class="service">Content Writing</li>
      <li class="service">E-mail</li>
      <li class="service">Social</li>
      <li class="service">SEO</li>
      <li class="service">Market Research</li>
    </ul>
    <div class="growth-illustration" role="img" aria-label="Illustration of a smartphone with a rising growth arrow"></div>
  </div>
</section>

<div class="divider"></div>

<section class="half half--back">
  <div class="card card--back">
    <header class="brand">
      <h1 class="brand__name">Kelvari Media</h1>
      <p class="brand__tagline">Marketing &amp; Sales Professional</p>
    </header>

    <div class="row row--dark row--mobile">
      <span>+65 84713095</span>
      <svg viewBox="0 0 20 20" aria-hidden="true"><rect x="5" y="1.5" width="10" height="17" rx="2" fill="none" stroke="currentColor" stroke-width="1.8"/><line x1="8.5" y1="15.5" x2="11.5" y2="15.5" stroke="currentColor" stroke-width="1.6"/></svg>
    </div>
    <div class="row row--yellow row--phone">
      <span>+65 84713095</span>
      <svg viewBox="0 0 20 20" aria-hidden="true"><path d="M2 7c0-2 3-3.5 8-3.5S18 5 18 7l-3 1.5-1-2H6l-1 2zM5 9h10l2 8H3z" fill="currentColor"/><circle cx="10" cy="13" r="2" fill="var(--yellow)"/></svg>
    </div>
    <div class="row row--dark row--address">
      <span>42 Lorong Tanah 319470</span>
      <svg viewBox="0 0 20 20" aria-hidden="true"><path d="M10 1.5a6 6 0 0 0-6 6c0 4.5 6 11 6 11s6-6.5 6-11a6 6 0 0 0-6-6z" fill="currentColor"/><circle cx="10" cy="7.5" r="2.3" fill="var(--charcoal)"/></svg>
    </div>

    <div class="row row--yellow row--name">
      <svg viewBox="0 0 20 20" aria-hidden="true"><circle cx="10" cy="6" r="3.5" fill="currentColor"/><path d="M3 18c0-4 3-7 7-7s7 3 7 7z" fill="currentColor"/></svg>
      <span>John doe</span>
    </div>
    <div class="row row--dark row--email">
      <svg viewBox="0 0 20 20" aria-hidden="true"><rect x="1.5" y="4" width="17" height="12" fill="none" stroke="currentColor" stroke-width="1.6"/><path d="M1.5 4l8.5 7 8.5-7" fill="none" stroke="currentColor" stroke-width="1.6"/></svg>
      <span>sales@kelvarimedia.com</span>
    </div>
    <div class="row row--yellow row--web">
      <svg viewBox="0 0 20 20" aria-hidden="true"><circle cx="10" cy="10" r="8" fill="none" stroke="currentColor" stroke-width="1.6"/><ellipse cx="10" cy="10" rx="3.5" ry="8" fill="none" stroke="currentColor" stroke-width="1.4"/><line x1="2" y1="10" x2="18" y2="10" stroke="currentColor" stroke-width="1.4"/></svg>
      <span>www.kelvarimedia.com</span>
    </div>
  </div>
</section>

</body>
</html>
```